Ferncrest Dental, LLC business card project

Business card to be designed with current logo.
Dental office- please keep design of card that looks clean and professional.
Please include the following info:
Ferncrest Dental, LLC
Dr. Lorna Pettigrew
2871 Marlowe Street
Bethlehem, PA 18093
610-555-0193
ferncrestdental.office@examplemail.test
Hello everyone-
Reason: Just got back from overseas- will look at all designs and provide feedback. Thank you!
Reason: Polling my friends for the final selection-
thank you to all those that participated- so many talented designers!

```html
<!DOCTYPE html>
<html lang="en">
<head>
<meta charset="utf-8">
<title>Ferncrest Dental, LLC — Business Card</title>
<link rel="stylesheet" href="https://fonts.googleapis.com/css2?family=Questrial&display=swap">
<style>
  :root {
    --canvas: #ffffff;
    --card-white: #ffffff;
    --card-border: #bdbdbd;
    --card-green: #b4d334;
    --brand-green: #5e9e2a;
    --name-green: #4f9a2a;
    --mark-green: #a7cf3a;
    --body-grey: #4a4a4a;
    --on-green: #ffffff;
    --logo-plate: rgba(255, 255, 255, 0.12);
  }
  html, body {
    margin: 0;
    padding: 0;
    width: 1200px;
    height: 900px;
    overflow: hidden;
    background: var(--canvas);
    font-family: "Questrial", "Century Gothic", sans-serif;
  }
  .canvas {
    position: relative;
    width: 1200px;
    height: 900px;
  }
  .card {
    position: absolute;
    top: 297px;
    width: 470px;
    height: 308px;
    box-sizing: border-box;
  }
  .card--front {
    left: 91px;
    background: var(--card-white);
    border: 1px solid var(--card-border);
  }
  .card--back {
    left: 641px;
    background: var(--card-green);
  }
  .brand {
    position: absolute;
    display: flex;
    align-items: center;
    gap: 12px;
    white-space: nowrap;
    letter-spacing: -0.5px;
  }
  .brand__dot {
    width: 26px;
    height: 26px;
    border-radius: 50%;
    flex: none;
  }
  .card--front .brand {
    left: 0;
    right: 0;
    top: 62px;
    justify-content: center;
    font-size: 38px;
    color: var(--brand-green);
  }
  .card--front .brand__dot { background: var(--mark-green); }
  .card--back .brand {
    left: 81px;
    top: 126px;
    width: 308px;
    height: 55px;
    justify-content: center;
    background: var(--logo-plate);
    font-size: 34px;
    color: var(--on-green);
  }
  .card--back .brand__dot { background: var(--on-green); width: 22px; height: 22px; }
  .contact {
    position: absolute;
    left: 0;
    right: 0;
    top: 194px;
    text-align: center;
  }
  .contact__names {
    margin: 0 0 9px;
    font-size: 15px;
    color: var(--name-green);
  }
  .contact__line {
    margin: 0;
    font-size: 13px;
    line-height: 16px;
    color: var(--body-grey);
  }
  .sep { margin: 0 4px; }
</style>
</head>
<body>
<main class="canvas">
  <section class="card card--front" aria-label="Card front">
    <div class="brand">
      <span class="brand__dot" aria-hidden="true"></span>
      <span class="brand__name">Ferncrest Dental</span>
    </div>
    <div class="contact">
      <p class="contact__names">Ferncrest Dental, LLC<span class="sep">|</span>Dr. Lorna Pettigrew</p>
      <p class="contact__line">2871 Marlowe Street, Bethlehem, PA 18093</p>
      <p class="contact__line">M : 610-555-0193<span class="sep">|</span>E : ferncrestdental.office@examplemail.test</p>
    </div>
  </section>

  <section class="card card--back" aria-label="Card back">
    <div class="brand">
      <span class="brand__dot" aria-hidden="true"></span>
      <span class="brand__name">Ferncrest Dental</span>
    </div>
  </section>
</main>
</body>
</html>
```